Steady Harbor Stewardship Graphics

We need help to design a logo, graphics, layout that will represent a particular type of leadership consulting business that we are about to launch. The design/graphics should be able to be used for developing a brochure, web page, advertisements, letterhead, business cards, etc. The leadership consulting business that we are launching is called “Steady Harbor Stewardship.” We would like to start with the design of a brochure. We have enclosed a draft to give you some ideas about the type of graphics we are looking for. The graphics should include fonts, colors, pictures/symbols, and layout initially for the brochure only. There are three draft pictures/symbols that we have gotten from the internet for the attached brochure that may be copyrighted. We would like you to develop something similar, but original for each of the graphic’s. They each represent a theme/topic that we will be using. For example, the graphic for the section titled “What is Steady Harbor Stewardship?” has a picture/graphic that has a diverse group of people to represent the idea of Collective Leadership. It leaves out some of the facial features for each person in order to make sure that there are no similarities to real persons. We need something similar to this. The graphic for “Why is Steady Harbor Stewardship important?”, uses a picture of “ice” and a “mouse.” “Mice and Ice” is a key metaphor that we will use in our business. We need something to represent this concept. The same is true for the third picture that represents ripples in water. After design of the brochure we may seek additional help for the web page and other items.

Target Market(s)

Government and business organizations

Colors

Designer to choose colors to be used in the design.

Requirements
Must have
• Brochure Design
Nice to have
• Logos

```html
<!DOCTYPE html>
<html lang="en">
<head>
<meta charset="utf-8">
<title>Steady Harbor Stewardship — Brochure &amp; Identity Board</title>
<link href="https://fonts.googleapis.com/css2?family=Raleway:wght@300;400;600;700&family=Pathway+Gothic+One&family=EB+Garamond&display=swap" rel="stylesheet">
<style>
  :root {
    --harbor-blue: #44749D;
    --signal-orange: #F68E55;
    --ink: #2b2b2b;
    --soft-ink: #444;
    --light-blue: #6f9fd4;
    --panel-grey: #eeeeec;
    --deep-teal: #1f4d66;
    --paper: #ffffff;
    --head-font: "Pathway Gothic One", "Arial Narrow", sans-serif;
    --body-font: "Raleway", Arial, sans-serif;
    --serif-font: "EB Garamond", Georgia, serif;
  }
  * { box-sizing: border-box; margin: 0; padding: 0; }
  html, body { width: 1200px; height: 1200px; overflow: hidden; background: var(--paper); }
  body { position: relative; font-family: var(--body-font); color: var(--ink); }

  .spread { position: absolute; left: 57px; width: 634px; height: 490px; box-shadow: 2px 3px 6px rgba(0,0,0,.35); overflow: hidden; background: var(--paper); }
  .spread--outside { top: 72px; }
  .spread--inside { top: 627px; }
  .panel { position: absolute; top: 0; height: 490px; overflow: hidden; }

  .head { font-family: var(--head-font); font-weight: 400; line-height: .95; }
  .centered { text-align: center; }
  .body-copy { font-size: 8.6px; line-height: 1.5; font-weight: 400; }
  .justified { text-align: justify; }

  /* Outside spread */
  .objectives { left: 0; width: 209px; background: linear-gradient(180deg, #2a1d14 0%, #4a3222 35%, #7a5234 62%, #5a3b25 100%); color: #fff; }
  .objectives .orange-wash { position: absolute; left: 0; top: 380px; width: 100%; height: 42px; background: rgba(246,142,85,.55); }
  .objectives .title { position: absolute; top: 22px; width: 100%; font-size: 22px; color: #fff; }
  .objectives .intro { position: absolute; top: 47px; left: 11px; right: 11px; color: #f3ece6; }
  .objectives .group { position: absolute; left: 0; width: 100%; text-align: center; font-size: 8.4px; line-height: 1.45; color: #f4ede6; }
  .objectives .group h3 { font-size: 8.6px; font-weight: 600; color: var(--light-blue); text-transform: uppercase; line-height: 1.35; }

  .programs { left: 209px; width: 212px; background: var(--paper); }
  .programs .title { position: absolute; top: 22px; width: 100%; font-size: 22px; color: var(--harbor-blue); }
  .programs .intro { position: absolute; top: 47px; left: 12px; right: 12px; color: var(--soft-ink); }
  .programs .group { position: absolute; left: 0; width: 100%; text-align: center; font-size: 8.2px; line-height: 1.4; color: var(--soft-ink); }
  .programs .group h3 { font-size: 8.4px; font-weight: 600; color: var(--signal-orange); text-transform: uppercase; }
  .contact-band { position: absolute; top: 380px; left: 0; width: 100%; height: 42px; background: var(--signal-orange); color: #fff; text-align: center; font-size: 8.6px; line-height: 1.45; padding-top: 8px; }
  .contact-band strong { font-weight: 700; }
  .small-wordmark { position: absolute; top: 436px; left: 0; width: 100%; display: flex; flex-direction: column; align-items: center; gap: 4px; }
  .small-wordmark .dot { width: 22px; height: 22px; border-radius: 50%; background: var(--harbor-blue); }
  .small-wordmark span { font-size: 6.5px; font-weight: 400; color: var(--harbor-blue); }

  .cover { left: 421px; width: 213px; }
  .cover-scene { position: absolute; inset: 0; background: linear-gradient(180deg, #7fb5d3 0%, #b6d4df 28%, #d9d3c2 45%, #e7c7a0 58%, #c49a72 70%, #4d3a2c 88%, #2b2520 100%); }
  .cover-wordmark { position: absolute; top: 28px; left: 0; width: 100%; display: flex; flex-direction: column; align-items: center; gap: 8px; }
  .cover-wordmark .dot { width: 56px; height: 56px; border-radius: 50%; background: var(--harbor-blue); }
  .cover-wordmark span { font-size: 13px; font-weight: 400; color: var(--harbor-blue); text-align: center; line-height: 1.2; }
  .cover-card { position: absolute; top: 278px; left: 8px; width: 196px; height: 189px; border-radius: 6px; background: var(--harbor-blue); color: #fff; text-align: center; padding-top: 22px; }
  .cover-card .line-small { font-size: 17px; }
  .cover-card .line-big { font-size: 30px; margin-top: 4px; }
  .cover-card .names { font-family: var(--serif-font); font-size: 15px; color: #e9a36e; line-height: 1.4; margin-top: 12px; }

  /* Inside spread */
  .what-is { left: 0; width: 213px; background: var(--paper); }
  .what-is .title { position: absolute; top: 22px; left: 23px; font-size: 19px; color: var(--signal-orange); }
  .what-is .lead { position: absolute; top: 86px; left: 23px; width: 80px; font-size: 8.6px; font-weight: 700; line-height: 1.35; color: var(--harbor-blue); }
  .what-is .sidebar { position: absolute; top: 80px; left: 110px; width: 103px; height: 230px; background: var(--panel-grey); padding: 7px 6px 0 9px; font-size: 7.6px; line-height: 1.45; color: var(--soft-ink); }
  .hands-photo { position: absolute; top: 310px; left: 0; width: 100%; height: 180px; background: linear-gradient(135deg, #3a4a52 0%, #8a6a55 40%, #b79479 60%, #4b5558 100%); }

  .why { left: 213px; width: 209px; background: var(--paper); }
  .snow-photo { position: absolute; top: 0; left: 0; width: 100%; height: 226px; background: linear-gradient(135deg, #9aa4aa 0%, #c9d3da 40%, #eef2f5 60%, #aab6bf 100%); }
  .why .title { position: absolute; top: 24px; left: 11px; font-size: 21px; color: #1f2a33; }
  .why .callout { position: absolute; top: 170px; left: 11px; width: 180px; font-size: 8.4px; font-weight: 700; line-height: 1.3; color: var(--harbor-blue); }
  .how .title { position: absolute; top: 243px; left: 11px; font-size: 21px; color: var(--harbor-blue); }
  .how .copy { position: absolute; top: 303px; left: 11px; width: 188px; font-size: 7.6px; line-height: 1.48; color: var(--soft-ink); }
  .how .copy p + p { margin-top: 9px; }

  .metaphor { left: 422px; width: 212px; }
  .mouse-photo { position: absolute; top: 0; left: 0; width: 100%; height: 226px; background: linear-gradient(160deg, #6b7a88 0%, #a8a9ad 40%, #8f8c90 65%, #3d4e60 100%); }
  .metaphor .story { position: absolute; top: 10px; left: 22px; width: 182px; font-size: 7.4px; line-height: 1.48; color: #fff; }
  .metaphor .story p + p { margin-top: 9px; }
  .water-band { position: absolute; top: 226px; left: 0; width: 100%; height: 264px; background: linear-gradient(180deg, #184a63 0%, #1f5a78 45%, #3b7fa0 70%, #163b52 100%); }
  .metaphor .tagline { position: absolute; top: 239px; left: 16px; width: 180px; font-size: 8.2px; font-weight: 700; line-height: 1.3; color: #fff; }

  /* Identity column */
  .identity-wordmark { position: absolute; top: 250px; left: 780px; width: 340px; display: flex; flex-direction: column; align-items: center; gap: 30px; }
  .identity-wordmark .dot { width: 190px; height: 190px; border-radius: 50%; background: var(--harbor-blue); }
  .identity-wordmark span { font-size: 36px; font-weight: 300; color: var(--harbor-blue); text-align: center; line-height: 1.15; }

  .swatch { position: absolute; left: 798px; width: 52px; height: 52px; border-radius: 50%; }
  .swatch--blue { top: 660px; background: var(--harbor-blue); }
  .swatch--orange { top: 740px; background: var(--signal-orange); }
  .swatch-spec { position: absolute; left: 880px; font-size: 14.5px; line-height: 1.28; color: #333; font-weight: 400; }
  .fonts-label { position: absolute; top: 855px; left: 797px; font-size: 20px; color: #222; }
  .fonts-list { position: absolute; top: 850px; left: 880px; font-size: 14.5px; line-height: 1.28; color: #333; }
</style>
</head>
<body>

<!-- Outside spread -->
<section class="spread spread--outside">
  <div class="panel objectives" role="img" aria-label="Photo of a brass compass on a wooden table">
    <div class="orange-wash"></div>
    <h2 class="head title centered">SHS OBJECTIVES</h2>
    <p class="body-copy justified intro">SHS is about cultivating and capturing collective leadership resources in order to help chart a course through the dangers and opportunities of our time. Its objectives are as follows:</p>
    <div class="group" style="top:126px"><h3>Improve Organizational<br>Navigation</h3>Avoid potential land mines<br>Exploit opportunities</div>
    <div class="group" style="top:189px"><h3>Increase Accountability</h3>Constituency Accountability<br>Outcome Accountability<br>Process Accountability</div>
    <div class="group" style="top:250px"><h3>Enhance Cooperation</h3>Create strong connections<br>Balance competition with cooperation<br>Incorporate strong, diverse individuals</div>
  </div>

  <div class="panel programs">
    <h2 class="head title centered">SHS PROGRAMS</h2>
    <p class="body-copy justified intro">SHS’s comprehensive approach to improving leadership is transformational. However, it need not be implemented in its entirety to realize its benefits. It can be customized to meet the needs of small to large groups.</p>
    <div class="group" style="top:124px"><h3>What does it include?</h3>Day long or Half day workshops<br>Multi-Day workshops<br>Instruction and coaching</div>
    <div class="group" style="top:180px"><h3>What are the programs about?</h3>Developing a SH Philosophy<br>Executing SH Processes<br>Growing SH Judgement<br>Leadership Roles for Everyone<br>Team Leadership<br>Building a SH Culture</div>
    <div class="group" style="top:270px"><h3>Who could benefit?</h3>Organizations<br>Professional Associations<br>Individuals, Teams and Small Groups</div>
    <div class="group" style="top:326px"><h3>How can it help?</h3>Identify leadership strengths and weaknesses.<br>Address leadership training needs.<br>Develop organizational leadership capacity.</div>
    <div class="contact-band">Dana Mercer: <strong>dmercer@harbormail.net</strong><br>Luis Ortega: <strong>lortega@harbormail.net</strong></div>
    <div class="small-wordmark"><div class="dot"></div><span>Steady Harbor Stewardship</span></div>
  </div>

  <div class="panel cover">
    <div class="cover-scene" role="img" aria-label="Photo of a calm lake at sunrise with birds flying in the sky"></div>
    <div class="cover-wordmark"><div class="dot"></div><span>Steady Harbor<br>Stewardship</span></div>
    <div class="cover-card">
      <div class="head line-small">IDENTIFY AND ENGAGE THE</div>
      <div class="head line-big">COLLECTIVE<br>LEADERSHIP</div>
      <div class="head line-small" style="margin-top:4px">IN YOUR ORGANIZATION</div>
      <div class="names">Dana Mercer<br>Luis Ortega</div>
    </div>
  </div>
</section>

<!-- Inside spread -->
<section class="spread spread--inside">
  <div class="panel what-is">
    <h2 class="head title">WHAT IS STEADY<br>HARBOR<br>STEWARDSHIP?</h2>
    <p class="lead">Leadership that cultivates and harvests collective human resources to help organizations navigate today’s uncertain world.</p>
    <div class="sidebar">Identifying, growing, and channeling human resources is the primary role of Leadership. Skillful navigation, improved accountability, and enhanced levels of cooperation are magnified when collective knowledge, wisdom, and creativity are employed. Most leadership literature revolves around building individual capabilities. SHS is about tapping into the often-latent collective leadership resources in organizations.</div>
    <div class="hands-photo" role="img" aria-label="Photo of a diverse group joining fists over a table"></div>
  </div>

  <div class="panel why">
    <div class="snow-photo" role="img" aria-label="Close-up photo of an ice crystal snowflake"></div>
    <h2 class="head title">WHY IS STEADY<br>HARBOR<br>STEWARDSHIP<br>IMPORTANT?</h2>
    <p class="callout">Cooperative, accountable organizations that are on track are better prepared to respond to the unprecedented dangers and opportunities of today’s world.</p>
    <div class="how">
      <h2 class="head title">HOW DOES STEADY HARBOR<br>STEWARDSHIP WORK?</h2>
      <div class="copy">
        <p>Like ripples through water, Leadership Influence penetrates an organization. Beneficial Leadership Influence has these characteristics; it must be positive, is both individual and collective, and both indirect and direct.</p>
        <p>Collective Leadership Influence begins with a Collective Leadership Philosophy, grows through Collective Leadership Processes, and matures with Collective Leadership Judgement.</p>
        <p>Who bears responsibility for propelling Collective Leadership Influence? Influence cannot happen without competent Influencers. The three most important are: individuals, teams, and culture.</p>
      </div>
    </div>
  </div>

  <div class="panel metaphor">
    <div class="mouse-photo" role="img" aria-label="Soft-focus photo of a small white mouse"></div>
    <div class="story">
      <p>It was ice that sunk the Titanic, the largest passenger ship afloat, on its maiden voyage in 1912. It was a mouse (not the furry kind) that revolutionized the personal computer industry in the 1980s.</p>
      <p>What do these two events have in common? They both involve course corrections. One to avoid the “ice”, and the other to not miss the “mice”.</p>
      <p>In a more amplified setting, today’s organizations face ice fields of danger along with oceans of possibility. Without skillful navigation, an organization is either left adrift and missing opportunities, or is propelling toward unintended destinations with possible dire consequences.</p>
    </div>
    <div class="water-band" role="img" aria-label="Photo of a water droplet sending ripples across dark blue water"></div>
    <p class="tagline">By cultivating and deploying positive Collective Leadership Influence through constructive Collective Leadership Influencers.</p>
  </div>
</section>

<!-- Identity -->
<div class="identity-wordmark"><div class="dot"></div><span>Steady Harbor<br>Stewardship</span></div>

<div class="swatch swatch--blue"></div>
<div class="swatch-spec" style="top:661px">C78&nbsp; M50&nbsp; Y21&nbsp; K2<br>R68&nbsp; G116&nbsp; B157<br>HEX #44749D</div>
<div class="swatch swatch--orange"></div>
<div class="swatch-spec" style="top:741px">C9&nbsp; M54&nbsp; Y72&nbsp; K0<br>R246&nbsp; G142&nbsp; B85<br>HEX #F68E55</div>

<div class="fonts-label">FONTS:</div>
<div class="fonts-list">Raleway Light<br>Raleway SemiBold</div>

</body>
</html>
```